BQL Groundworks & Freight Business Card

Can you please design a business card for an Earthworks, Haulage truck and machinery hire company. They also provide sand soil and mulch supply, as well as screening of products. Can you re-create the logo from the attached but add BQL Groundworks & Freight just use the three diamond design.

Target Market(s)

Earthmoving and Transport, Landscapers, Construction

Contact Information for Business Card

ABN 52 907 334 816, Doug Pelham, Managing Director, BQL Groundworks & Freight Mobile 0438 256 904 Email bqlfreight2010@mailvane.net

Font styles to use
Sans Serif

Colors
ec1f27
000000
cbcbcb
ffffff

Requirements
Must have
• Listed on the back, Earthworks | Haulage | Truck and Machinery Hire | Sand, Soil & Mulch Supply | Screening of Products
Nice to have
• Would be good for it to look appealing to a mans man, because it relates to heavy machinery, earthworks, construction etc. Black, red and white would be good maybe with a bit of silver somewhere.
Should not have
• not sure

```html
<!DOCTYPE html>
<html lang="en">
<head>
<meta charset="utf-8">
<title>BQL Groundworks &amp; Freight Business Card</title>
<link rel="stylesheet" href="https://fonts.googleapis.com/css2?family=Questrial&display=swap">
<style>
  :root {
    --red: #ec1f27;
    --red-deep: #c81a22;
    --black: #000000;
    --silver: #cbcbcb;
    --white: #ffffff;
    --backdrop: #e9e9e9;
  }
  * { box-sizing: border-box; margin: 0; padding: 0; }
  html, body {
    width: 1200px; height: 801px; overflow: hidden;
    background: var(--backdrop);
    font-family: "Questrial", Arial, sans-serif;
  }
  .sheet {
    position: relative; width: 1200px; height: 801px;
    display: flex; align-items: center; justify-content: center; gap: 40px;
  }
  .card {
    position: relative; width: 500px; height: 286px;
    background: var(--white); overflow: hidden;
    box-shadow: 0 2px 10px rgba(0,0,0,0.15);
  }

  /* Front: services */
  .front-brand {
    position: absolute; left: 0; top: 0; width: 215px; height: 100%;
    display: flex; align-items: center; justify-content: center;
  }
  .brand-mark { display: flex; align-items: center; gap: 8px; color: var(--red); }
  .brand-mark .square { width: 14px; height: 14px; background: var(--red); flex: none; }
  .brand-mark .name { font-size: 15px; line-height: 1.2; letter-spacing: 0.02em; }
  .front-panel {
    position: absolute; left: 215px; top: 0; right: 0; bottom: 0;
    background: linear-gradient(160deg, var(--red), var(--red-deep));
  }
  .front-panel::before {
    content: ""; position: absolute; left: 8px; top: 0; bottom: 0;
    width: 3px; background: var(--white);
  }
  .services {
    position: absolute; left: 44px; top: 50%; transform: translateY(-50%);
    list-style: none; color: var(--white); font-size: 17px; line-height: 1.15;
  }
  .services li { position: relative; padding-left: 22px; margin-bottom: 4px; }
  .services li::before {
    content: ""; position: absolute; left: 0; top: 8px;
    width: 3px; height: 3px; border-radius: 50%; background: var(--white);
  }

  /* Back: contact */
  .back-top { position: absolute; left: 0; top: 0; right: 0; height: 132px; }
  .person { position: absolute; left: 30px; top: 30px; color: var(--black); }
  .person .full-name { font-size: 32px; font-weight: 400; letter-spacing: 0.01em; }
  .person .role { font-size: 19px; margin-top: 4px; }
  .back-top .brand-mark { position: absolute; right: 26px; bottom: 12px; }
  .back-top .brand-mark .name { font-size: 13px; }
  .rule { position: absolute; left: 0; right: 0; top: 132px; height: 5px; background: var(--red); }
  .back-panel {
    position: absolute; left: 0; right: 0; top: 142px; bottom: 0;
    background: linear-gradient(160deg, var(--red), var(--red-deep));
  }
  .contact {
    position: absolute; left: 30px; top: 24px;
    list-style: none; color: var(--white); font-size: 16px; line-height: 1.9;
  }
  .contact .label { text-transform: uppercase; }
</style>
</head>
<body>
<main class="sheet">
  <section class="card card-front" aria-label="Card front">
    <div class="front-brand">
      <div class="brand-mark"><span class="square"></span><span class="name">BQL Groundworks<br>&amp; Freight</span></div>
    </div>
    <div class="front-panel">
      <ul class="services">
        <li>Earthworks</li>
        <li>Haulage</li>
        <li>Truck and<br>Machinery Hire</li>
        <li>Sand, Soil &amp; Mulch<br>Supply</li>
        <li>Screening of<br>Products</li>
      </ul>
    </div>
  </section>

  <section class="card card-back" aria-label="Card back">
    <div class="back-top">
      <div class="person">
        <h1 class="full-name">Doug Pelham</h1>
        <p class="role">Managing Director</p>
      </div>
      <div class="brand-mark"><span class="square"></span><span class="name">BQL Groundworks &amp; Freight</span></div>
    </div>
    <div class="rule"></div>
    <div class="back-panel">
      <ul class="contact">
        <li><span class="label">Mobile:</span> 0438 256 904</li>
        <li><span class="label">Email:</span> bqlfreight2010@mailvane.net</li>
        <li><span class="label">ABN:</span> 52 907 334 816</li>
      </ul>
    </div>
  </section>
</main>
</body>
</html>
```